Web Developer Needs a Business Card Design

I need a personal business card design that represents me as a web developer for potential employers. I would like the background to be a dark color on the front for contrast with my logo and name. The back will have all my information along with a smaller version of the logo. I want something with a modern look and feel, not too conservative. This will be used for potential employers and freelance work.

Industry/Entity Type

Business

Contact Information for Business Card

Front should have my logo and name. The back should have all my personal information which would include: name: Tom Varnuch, phone: 570-614-9083, email: tomvarnuch@mailnest.example, website url: www.tomvarnuch.example, logo, web developer.

Font styles to use
Sans Serif

Requirements
Must have
• Must include my logo. The color palette base color will be the logo color.

```html
<!DOCTYPE html>
<html lang="en">
<head>
<meta charset="utf-8">
<title>Tom Varnuch — Business Card</title>
<link href="https://fonts.googleapis.com/css2?family=Questrial&family=Roboto:wght@300&display=swap" rel="stylesheet">
<style>
  :root {
    --backdrop: #8a8c8b;
    --card-dark: #121414;
    --pattern-tone: #1c2b27;
    --photo-left: #3a3a3a;
    --photo-right: #2a2220;
    --teal: #4ecfa8;
    --name-ink: #e6e6e6;
    --subtitle-ink: #b9b9b9;
  }
  * { box-sizing: border-box; margin: 0; padding: 0; }
  html, body {
    width: 1200px; height: 900px; overflow: hidden;
    background: var(--backdrop);
  }
  .stage { position: relative; width: 1200px; height: 900px; }
  .card {
    position: absolute; left: 321px; width: 507px; height: 289px;
    overflow: hidden; background: var(--card-dark);
  }
  .card--front { top: 119px; }
  .card--back { top: 471px; }

  .front-pattern {
    position: absolute; inset: 0;
    background: radial-gradient(circle at 50% 50%, var(--pattern-tone) 0%, var(--card-dark) 85%);
  }
  .brand {
    position: absolute; display: flex; align-items: center; gap: 10px;
    font-family: "Questrial", sans-serif; color: var(--teal); white-space: nowrap;
  }
  .brand__dot {
    width: 16px; height: 16px; border-radius: 50%;
    border: 3px solid var(--teal);
  }
  .card--front .brand {
    left: 50%; top: 50%; transform: translate(-50%, -50%);
    font-size: 26px; letter-spacing: 0.5px;
  }

  .back-photo {
    position: absolute; inset: 0;
    background: linear-gradient(90deg, var(--photo-left) 0%, #2f2d2c 45%, var(--photo-right) 100%);
  }
  .card--back .brand {
    left: 381px; top: 54px; transform: translate(-50%, -50%);
    font-size: 20px;
  }
  .identity {
    position: absolute; right: 35px; top: 118px; text-align: right;
    font-family: "Roboto", sans-serif; font-weight: 300;
  }
  .identity__name {
    font-size: 24px; letter-spacing: 1px; color: var(--name-ink);
    text-transform: uppercase;
  }
  .identity__role {
    margin-top: 10px; margin-right: 25px;
    font-size: 13px; letter-spacing: 0.6px; color: var(--subtitle-ink);
  }
  .divider {
    position: absolute; left: 36px; right: 35px; top: 196px;
    height: 1px; background: var(--teal); opacity: 0.8;
  }
  .contacts {
    position: absolute; top: 212px; list-style: none;
    font-family: "Questrial", sans-serif; font-size: 14.5px; color: var(--teal);
  }
  .contacts--main { left: 33px; }
  .contacts--social { left: 323px; }
  .contacts li {
    display: flex; align-items: center; gap: 8px; height: 20px;
  }
  .contacts svg { width: 13px; height: 13px; flex: none; }
  .social-dot {
    width: 12px; height: 12px; border-radius: 50%; background: var(--teal); flex: none;
  }
</style>
</head>
<body>
<main class="stage">

  <section class="card card--front" aria-label="Card front">
    <div class="front-pattern" role="img" aria-label="Repeating tonal pattern of the personal mark on a dark ground"></div>
    <div class="brand"><span class="brand__dot"></span>Tom Varnuch</div>
  </section>

  <section class="card card--back" aria-label="Card back">
    <div class="back-photo" role="img" aria-label="Dim overhead photo of a laptop keyboard and a cup of coffee on a dark desk"></div>
    <div class="brand"><span class="brand__dot"></span>Tom Varnuch</div>

    <div class="identity">
      <h1 class="identity__name">Tom Varnuch</h1>
      <p class="identity__role">Front-End Developer</p>
    </div>

    <div class="divider"></div>

    <ul class="contacts contacts--main">
      <li>
        <svg viewBox="0 0 16 16" aria-hidden="true"><path fill="currentColor" d="M3.6 1.2l2.3 2.6-1.3 1.7c.8 1.8 2.1 3.1 3.9 3.9l1.7-1.3 2.6 2.3-1 2.6C6.4 13.2 2.8 9.6 1 4.2z"/></svg>
        570-614-9083
      </li>
      <li>
        <svg viewBox="0 0 16 16" aria-hidden="true"><rect x="1" y="3" width="14" height="10" fill="currentColor"/><path d="M1.5 3.5L8 9l6.5-5.5" stroke="#2d2b2a" stroke-width="1.4" fill="none"/></svg>
        tomvarnuch@mailnest.example
      </li>
      <li>
        <svg viewBox="0 0 16 16" aria-hidden="true"><circle cx="8" cy="8" r="7" fill="currentColor"/><path d="M1 8h14M8 1c-3 3.5-3 10.5 0 14M8 1c3 3.5 3 10.5 0 14" stroke="#2d2b2a" stroke-width="1" fill="none"/></svg>
        www.tomvarnuch.example
      </li>
    </ul>

    <ul class="contacts contacts--social">
      <li><span class="social-dot"></span>@tomvarnuch.example</li>
      <li><span class="social-dot"></span>tomvarnuch.example</li>
      <li><span class="social-dot"></span>tomvarnuch.example</li>
    </ul>
  </section>

</main>
</body>
</html>
```